依頼詳細
配食事業の広告のリニューアル(価格改定)と
キャンペーン広告展開を予定しています。
内容は現行のチラシを参考にコピーやレイアウトなど
多彩で自由な提案を期待しています。

写真は複数点アップロードしていますが
適当なものを使用下さい。

<通常版>
●現行チラシからの要変更点
①お弁当の写真※写真データを添付。写真は1個使用でも2個使用でも構いません。
②弁当価格(現行670円→変更後750円)
③献立例※写真の内容
◇昼食の献立例 301Kcal
■豚肉のねぎ塩炒め■冬瓜の蟹あんかけ■スパゲティサラダ■漬物
◇夕食の献立例 264Kcal
■鶏の黄金焼き■こんにゃくの土佐煮■ほうれん草のなめ茸和え■漬物
④・注文から~お支払いの流れ
・お申し込み欄
・ご注意事項
は必須記載でお願いいたします。

<キャンペーン版>
上記通常版をベースに下記のキャンペーン内容を盛り込んでPR願います。
●キャンペーン内容
「5食500円引き お弁当お試しキャンペーン」
■キャンペーン対象:陽報販売所から初めてご注文される方
■下記期間内で5食以上ご注文いただける方
■期間:4月14日(金)~5月12日(金)
■キャンペーン利用は期間中1世帯1回のみとなります。

記載項目
依頼詳細欄を参照ください。
サイズ
概要・特徴をご参照下さい
ページ数
片面
希望イメージ
シンプル 複雑
単色 カラフル
暗い 明るい
日常 高級
遊び心 厳粛
未来的 伝統的
女性的 男性的
希望する色
赤系、黄・オレンジ系、茶系、お弁当が美味しそうに見える色
納品ファイル
• 高解像度JPG (.jpg)
• イラストレーター形式 (.ai)
補足説明
上記に加え、PDFデータ納品もお願いいたします。
記載に間違いがありました。
>まずは現行チラシのPDFデータと写真を使い、
ベースとなるA4チラシで①と②を作成ください。

とありますがベースはB4で作成をお願いいたします。

またaiデータも添付しますのでこちらも適宜使用願います。

どうぞよろしくお願いいたします。

シンプルなデザインにオリジナルのアイコンやコピーなどを評価し、選定させていただきました。

短期間に様々なご提案をいただき、ありがとうございます。
これからも同様の案件をご依頼するかと思います。
機会がありましたら次回以降もどうぞよろしくお願いいたします。

```html
<!DOCTYPE html>
<html lang="ja">
<head>
<meta charset="utf-8">
<title>自社で手づくりのお弁当 お届けします</title>
<link href="https://fonts.googleapis.com/css2?family=M+PLUS+Rounded+1c:wght@400;700;800&family=Noto+Sans+JP:wght@400;700;900&display=swap" rel="stylesheet">
<style>
:root{
  --orange:#ef7d1a;
  --orange-deep:#e0601a;
  --red:#e2381f;
  --yellow:#fde04a;
  --cream:#fff6dc;
  --brown:#5a3a1f;
  --ink:#333;
  --line:#f2b26b;
  --photo-cool:#c7ccd1;
}
*{box-sizing:border-box;margin:0;padding:0}
html,body{width:857px;height:1200px;overflow:hidden;background:#fff}
body{font-family:"Noto Sans JP",sans-serif;color:var(--ink);position:relative}
.flyer{position:absolute;inset:0;width:857px;height:1200px;overflow:hidden}

/* header */
.brand{position:absolute;left:24px;top:16px;display:flex;align-items:center;gap:10px}
.brand-dot{width:46px;height:46px;border-radius:50%;background:var(--orange)}
.brand-name{font-family:"M PLUS Rounded 1c",sans-serif;font-weight:800;font-size:24px;color:var(--brown)}
.ribbon{position:absolute;left:250px;top:14px;width:310px;height:56px;background:var(--orange);color:#fff;
  font-family:"M PLUS Rounded 1c",sans-serif;font-weight:800;font-size:34px;display:flex;align-items:center;justify-content:center;
  clip-path:polygon(0 0,100% 0,95% 50%,100% 100%,0 100%,5% 50%)}
.joy{position:absolute;left:600px;top:16px;width:230px;height:54px;border:2px solid var(--orange);border-radius:6px;
  font-family:"M PLUS Rounded 1c",sans-serif;font-weight:700;font-size:16px;color:var(--brown);
  display:flex;align-items:center;justify-content:center;gap:4px;white-space:nowrap}
.joy b{color:var(--red);font-size:24px}

/* hero */
.couple{position:absolute;left:470px;top:84px;width:360px;height:196px;border-radius:14px;background:linear-gradient(160deg,#f7e6cf,#e9cfa8)}
.badge-health{position:absolute;left:722px;top:168px;width:104px;height:104px;border-radius:50%;background:#fff;border:3px solid var(--orange);
  color:var(--orange-deep);font-weight:700;font-size:14px;line-height:1.35;display:flex;align-items:center;justify-content:center;text-align:center}
.lead{position:absolute;left:50px;top:130px;font-family:"M PLUS Rounded 1c",sans-serif;font-weight:800;font-size:36px;color:var(--brown)}
.title{position:absolute;left:40px;top:170px;font-family:"M PLUS Rounded 1c",sans-serif;font-weight:800;font-size:74px;color:var(--red);letter-spacing:4px}
.daily{position:absolute;left:30px;top:262px;width:320px;height:40px;background:var(--yellow);color:var(--red);
  font-family:"M PLUS Rounded 1c",sans-serif;font-weight:800;font-size:26px;display:flex;align-items:center;justify-content:center}
.per{position:absolute;left:40px;top:312px;background:var(--red);color:#fff;font-size:15px;font-weight:700;padding:3px 10px}
.price{position:absolute;left:40px;top:334px;color:var(--red);font-family:"M PLUS Rounded 1c",sans-serif;font-weight:800;font-size:92px;line-height:1}
.price small{font-size:52px}
.price-note{position:absolute;left:40px;top:432px;font-size:15px;color:var(--red);font-weight:700}
.price-note span{font-size:12px;color:var(--ink);font-weight:400;margin-left:6px}
.points{position:absolute;left:40px;top:462px;width:310px;list-style:none;font-size:12px;line-height:1.7}
.points li{display:flex;gap:6px;align-items:center}
.points li::before{content:"";width:9px;height:9px;background:var(--orange);border-radius:2px;flex:none}
.notice{position:absolute;left:40px;top:550px;width:310px;background:var(--cream);border:1px solid var(--line);font-size:11px;line-height:1.6;padding:8px 10px}

.bento-lunch{position:absolute;left:372px;top:300px;width:195px;height:230px;border-radius:6px;background:linear-gradient(150deg,#c8352a,#7e1f18)}
.bento-dinner{position:absolute;left:585px;top:292px;width:245px;height:178px;border-radius:6px;background:linear-gradient(150deg,#3d3a36,#8f7a5a)}
.menu-tag{position:absolute;background:#fff;border:1px solid var(--line);font-size:10px;line-height:1.5;padding:4px 6px;border-radius:4px}
.menu-tag b{color:var(--orange-deep);display:block;font-size:11px}
.tag-lunch{left:380px;top:540px;width:180px}
.tag-dinner{left:700px;top:478px;width:130px}
.nutrition{position:absolute;left:585px;top:500px;width:100px;height:120px;border-radius:8px;background:linear-gradient(160deg,#f0e2d0,#d4b896)}
.nutrition-copy{position:absolute;left:690px;top:550px;width:140px;text-align:right}
.nutrition-copy .sup{display:block;font-size:11px;color:var(--red);font-weight:700;line-height:1.4;margin-bottom:3px}
.nutrition-copy .main{font-family:"M PLUS Rounded 1c",sans-serif;font-weight:800;font-size:18px;color:var(--brown);line-height:1.3}

/* flow */
.flow-band{position:absolute;left:0;top:660px;width:857px;height:42px;background:var(--orange);color:#fff;
  font-family:"M PLUS Rounded 1c",sans-serif;font-weight:800;font-size:24px;display:flex;align-items:center;justify-content:center}
.steps{position:absolute;left:24px;top:716px;width:809px;display:flex;gap:22px}
.step{flex:1;height:126px;border:2px solid var(--line);border-radius:8px;padding:10px 12px;position:relative;background:#fff}
.step-no{position:absolute;left:-10px;top:-10px;width:34px;height:34px;border-radius:50%;background:var(--red);color:#fff;font-weight:900;font-size:20px;display:flex;align-items:center;justify-content:center}
.step h3{font-size:15px;color:var(--orange-deep);margin:4px 0 6px 22px}
.step p{font-size:11.5px;line-height:1.6}
.arrow{position:absolute;right:-20px;top:48px}

/* bottom */
.bottom-copy{position:absolute;left:30px;top:862px;width:320px;font-size:15px;font-weight:700;color:var(--red);line-height:1.5}
.staff{position:absolute;left:30px;top:935px;width:320px;height:140px;border-radius:8px;background:linear-gradient(160deg,var(--photo-cool),#9aa3ab)}
.bottom-note{position:absolute;left:30px;top:1082px;width:320px;font-size:11px;line-height:1.55}
.contact{position:absolute;left:430px;top:862px;width:400px;height:112px;border:3px solid var(--orange);border-radius:10px;padding:10px 16px}
.contact-label{font-size:13px;color:var(--brown);font-weight:700}
.tel{display:flex;align-items:center;gap:8px;color:var(--red);font-family:"M PLUS Rounded 1c",sans-serif;font-weight:800;font-size:40px;line-height:1.2}
.tel small{font-size:22px}
.contact-name{font-size:16px;font-weight:900;color:var(--brown)}
.caution{position:absolute;left:430px;top:986px;width:400px;font-size:10.5px;line-height:1.6}
.caution h4{font-size:12px;color:var(--orange-deep);margin-bottom:2px}
.company{position:absolute;left:30px;top:1150px;font-size:11px;color:#555}
.back-btn{position:absolute;left:590px;top:1140px;width:240px;height:40px;background:var(--orange);color:#fff;
  font-weight:700;font-size:18px;display:flex;align-items:center;justify-content:center;gap:8px;border-radius:4px}
</style>
</head>
<body>
<div class="flyer">
  <header>
    <div class="brand"><span class="brand-dot"></span><span class="brand-name">ひだまり便</span></div>
    <div class="ribbon">お届けします!</div>
    <div class="joy">日々の<b>「食」</b>するよろこび。</div>
  </header>

  <section class="hero">
    <div class="couple" role="img" aria-label="笑顔の高齢のご夫婦のイラスト"></div>
    <div class="badge-health">健康な<br>高齢者様<br>向けに好評</div>
    <p class="lead">自社で手づくりの</p>
    <h1 class="title">お弁当</h1>
    <p class="daily">毎日の昼食/夕食を</p>
    <p class="per">1食(昼食/夕食)あたり</p>
    <p class="price"><small>¥</small>750</p>
    <p class="price-note">おかず+ごはん<span>(税込み・お届け料込み)</span></p>
    <ul class="points">
      <li>お弁当は毎日手づくりしています</li>
      <li>容器は電子レンジで温められます</li>
      <li>1食からご自宅までお届けします</li>
    </ul>
    <div class="notice">お届けは月曜日から土曜日となります。日曜・祝日はお休みです。配達地域はお問い合わせください。</div>

    <div class="bento-lunch" role="img" aria-label="昼食のお弁当の写真"></div>
    <div class="menu-tag tag-lunch"><b>昼食の献立例 301Kcal</b>豚肉のねぎ塩炒め・冬瓜の蟹あんかけ・スパゲティサラダ・漬物</div>
    <div class="bento-dinner" role="img" aria-label="夕食のお弁当の写真"></div>
    <div class="menu-tag tag-dinner"><b>夕食の献立例 264Kcal</b>鶏の黄金焼き・こんにゃくの土佐煮・ほうれん草のなめ茸和え・漬物</div>
    <div class="nutrition" role="img" aria-label="管理栄養士の写真"></div>
    <div class="nutrition-copy">
      <span class="sup">メニューはすべて<br>管理栄養士が監修</span>
      <p class="main">栄養士が考えた<br>バランスよい食事</p>
    </div>
  </section>

  <section class="flow">
    <h2 class="flow-band">ご注文から、お食事のお届け、お支払いまでの流れ</h2>
    <div class="steps">
      <div class="step"><span class="step-no">1</span><h3>お電話でご注文</h3><p>陽報販売所までお電話ください。お届け日と食数をうかがいます。</p>
        <svg class="arrow" width="18" height="24" viewBox="0 0 18 24"><path d="M2 2 L16 12 L2 22 Z" fill="#ef7d1a"/></svg></div>
      <div class="step"><span class="step-no">2</span><h3>ご自宅へお届け</h3><p>ご指定の時間にスタッフがお弁当を直接お届けします。</p>
        <svg class="arrow" width="18" height="24" viewBox="0 0 18 24"><path d="M2 2 L16 12 L2 22 Z" fill="#ef7d1a"/></svg></div>
      <div class="step"><span class="step-no">3</span><h3>月末にお支払い</h3><p>ひと月分をまとめて、翌月初めに集金にうかがいます。</p></div>
    </div>
  </section>

  <section class="bottom">
    <p class="bottom-copy">お弁当づくり、ご注文受付、お届けまで陽報販売所が行っております。</p>
    <div class="staff" role="img" aria-label="販売所スタッフの集合写真"></div>
    <p class="bottom-note">お気軽にお問い合わせください。スタッフ一同、心をこめてお届けします。</p>

    <div class="contact">
      <p class="contact-label">ご注文・お問い合わせは</p>
      <p class="tel">
        <svg width="32" height="32" viewBox="0 0 24 24"><path fill="#e2381f" d="M6.6 10.8a15 15 0 0 0 6.6 6.6l2.2-2.2a1 1 0 0 1 1-.25 11.4 11.4 0 0 0 3.6.57 1 1 0 0 1 1 1V20a1 1 0 0 1-1 1A17 17 0 0 1 3 4a1 1 0 0 1 1-1h3.5a1 1 0 0 1 1 1c0 1.25.2 2.45.57 3.6a1 1 0 0 1-.25 1z"/></svg>
        <small>TEL</small>011-555-0142</p>
      <p class="contact-name">陽報新聞販売所</p>
    </div>
    <div class="caution">
      <h4>ご注意事項</h4>
      <p>・ご注文の変更・取消は前日の正午までにお願いします。<br>・お届け後はお早めにお召し上がりください。<br>・食物アレルギーの個別対応はできかねます。<br>・天候等によりお届けが遅れる場合があります。</p>
    </div>
    <p class="company">調理・製造 みのり食品株式会社 札幌市中央区北一条西1丁目1-1</p>
    <div class="back-btn">献立表は裏面へ
      <svg width="14" height="18" viewBox="0 0 14 18"><path d="M2 2 L12 9 L2 16 Z" fill="#fff"/></svg></div>
  </section>
</div>
</body>
</html>
```